Business card and company stationary - Corvane Cleaning Ltd

1. Who are we and who are our customers?

o We are a relatively new cleaning company, established December 2008. We are a small company. We have 24 staff and we offer domestic and commercial cleaning services.
o We both (me and my wife) have been working for many years in the cleaning industry. We worked for some of the biggest and best cleaning companies in UK. We’ve been operatives, supervisors and managers.
o Inevitably after so many years of working for someone else, we decided to start our own business.
o Our domestic customers are middle class families and busy professionals. We’ve got some commercial customers, mainly offices.
o We are growing steadily.

2. What do we do? What are our services?

o Cleaning. We’ve got range of services - not to many but still can be daunting and confusing for some.
o Generally we’ve got domestic and commercial clients. The approach to the domestic cleaning customers is different to the commercial. In the way we want to say that it is cleaning that we do, but we acknowledge the environment and we appreciate the personal circumstances and requirements that are present. We do care, we listen and we try to work out the best possible way to complete our work.
o Mainly we get our work through referrals

3. What do we want with our stationery ?

o To place and maintain our message and reach out to people and organisations
o We want to advertise, communicate and sale.
o We are going to sell services.
o Increase membership, loyalty and support.

We are after business card design, headed letter and compliment slip.
We would like the headed letter to be created in formats suitable for :
- printing format
- also for use in our daily correspondence via e mail with clients and staff in a easy to edit and write format

The website we have is still under contraction and the domain is corvanecleaning.example

Target Market(s)

Families, individuals, businesses.

Industry/Entity Type

Cleaning Service

Contact Information for Business Card

FRONT :
Company Name - Corvane Cleaning Ltd
Company address - 41 Pelbury Rd, Pelbury, Essex, RM14 7QT
Name - Mrs. Teodora Vasilkova - Tedi
Title - Managing Director
Company phone - 020 8837 2591
E mail - tedi.vasilkova@corvanecleaning.example

BACK :

Company website - corvanecleaning.example
E mail - enquiries@corvanecleaning.example

Font styles to use
Serif

Requirements
Must have
• The above items and company logo...maybe at the back. But I'm free for any suggestions.

```html
<!DOCTYPE html>
<html lang="en">
<head>
<meta charset="utf-8">
<title>Corvane Cleaning Ltd – Stationery</title>
<link rel="stylesheet" href="https://fonts.googleapis.com/css2?family=Open+Sans:wght@400;600;700&family=Noto+Serif:wght@400;700&display=swap">
<style>
  :root{
    --bg:#e4e5e7;
    --paper:#ffffff;
    --blue:#1f74c4;
    --blue-deep:#1659a8;
    --blue-light:#58b4ea;
    --blue-pale:#a9d8f5;
    --ink:#2b2b2b;
    --watermark:#eef0f2;
  }
  *{box-sizing:border-box;margin:0;padding:0}
  html,body{width:1200px;height:960px;overflow:hidden;background:var(--bg)}
  body{position:relative;font-family:"Open Sans",Arial,sans-serif;color:var(--ink)}
  .sheet{position:absolute;background:var(--paper);overflow:hidden;box-shadow:0 2px 10px rgba(0,0,0,.15)}
  .sheet svg.waves{position:absolute;inset:0;width:100%;height:100%}
  .brand{position:absolute;display:flex;align-items:center;gap:8px}
  .brand-dot{border-radius:50%;border:2px solid var(--blue-deep);background:var(--paper);flex:none}
  .brand-name{font-family:"Open Sans",Arial,sans-serif;font-weight:700;color:var(--blue);line-height:1.05;letter-spacing:.04em;text-transform:uppercase}
  .contacts{position:absolute;font-size:11px;color:var(--ink);line-height:1.75}
  .contacts .row{display:flex;align-items:center;gap:14px;white-space:nowrap}
  .item{display:inline-flex;align-items:center;gap:5px}
  .ico{width:11px;height:11px;border-radius:50%;background:var(--blue);flex:none;display:inline-flex;align-items:center;justify-content:center}
  .ico svg{width:7px;height:7px}

  /* headed letter */
  .letterhead{left:60px;top:140px;width:480px;height:679px}
  .letterhead .brand{left:28px;top:26px}
  .letterhead .brand-dot{width:40px;height:40px}
  .letterhead .brand-name{font-size:19px}
  .letterhead .contacts{left:210px;bottom:26px}

  /* business card back */
  .card-back{left:590px;top:140px;width:290px;height:188px;background:linear-gradient(160deg,var(--blue-light) 0%,var(--blue) 55%,var(--blue-deep) 100%)}
  .card-back .brand{left:36px;top:52px}
  .card-back .brand-dot{width:36px;height:36px;border-color:var(--paper);background:transparent}
  .card-back .brand-name{color:var(--paper);font-size:17px}
  .card-back .tagline{position:absolute;left:0;right:0;top:108px;text-align:center;font-family:"Noto Serif",Georgia,serif;font-size:10.5px;color:var(--paper)}

  /* business card front */
  .card-front{left:900px;top:140px;width:290px;height:188px}
  .card-front .brand{left:14px;top:14px}
  .card-front .brand-dot{width:24px;height:24px}
  .card-front .brand-name{font-size:11.5px}
  .card-front .person{position:absolute;right:16px;top:64px;text-align:right;font-family:"Noto Serif",Georgia,serif;line-height:1.25}
  .card-front .person-name{font-size:14px;font-weight:700;color:var(--blue-deep)}
  .card-front .person-title{font-size:9px;color:var(--ink)}
  .card-front .contacts{right:16px;top:136px;font-size:8px;line-height:1.5;text-align:right}
  .card-front .contacts .row{justify-content:flex-end;gap:8px}
  .card-front .ico{width:10px;height:10px}

  /* compliment slip */
  .slip{left:590px;top:536px;width:600px;height:283px}
  .slip .mark-faint{position:absolute;right:40px;top:40px;width:230px;height:230px;border-radius:50%;border:10px solid var(--watermark)}
  .slip .brand{right:40px;top:96px}
  .slip .brand-dot{width:44px;height:44px}
  .slip .brand-name{font-size:22px}
  .slip .contacts{left:20px;top:154px;font-size:10.5px}
</style>
</head>
<body>

<!-- Headed letter -->
<section class="sheet letterhead" aria-label="Headed letter">
  <svg class="waves" viewBox="0 0 480 679" preserveAspectRatio="none" aria-hidden="true">
    <defs>
      <linearGradient id="lhTop" x1="0" y1="0" x2="1" y2="0">
        <stop offset="0" stop-color="var(--blue-deep)"/>
        <stop offset=".6" stop-color="var(--blue)"/>
        <stop offset="1" stop-color="var(--blue-light)"/>
      </linearGradient>
      <linearGradient id="lhBot" x1="0" y1="0" x2="1" y2="1">
        <stop offset="0" stop-color="var(--blue-light)"/>
        <stop offset="1" stop-color="var(--blue-deep)"/>
      </linearGradient>
    </defs>
    <path d="M0,86 C90,150 200,160 300,170 C380,178 440,190 480,210 L480,250 C420,228 360,218 290,212 C180,202 80,180 0,122 Z" fill="url(#lhTop)"/>
    <path d="M0,128 C80,186 180,208 290,218 C360,224 420,234 480,256 L480,266 C420,244 360,232 290,226 C180,216 80,196 0,140 Z" fill="var(--blue-light)"/>
    <path d="M0,146 C80,202 180,222 290,232 C360,238 420,248 480,270 L480,274 C420,254 360,243 290,237 C180,228 80,208 0,152 Z" fill="var(--blue-pale)"/>
    <path d="M0,540 C80,552 140,600 170,679 L0,679 Z" fill="url(#lhBot)"/>
    <path d="M0,588 C60,600 110,630 138,679 L128,679 C100,636 56,610 0,600 Z" fill="var(--blue-pale)"/>
    <path d="M0,610 C50,620 92,646 114,679 L108,679 C86,650 46,628 0,618 Z" fill="var(--blue-light)"/>
  </svg>
  <div class="brand">
    <span class="brand-dot"></span>
    <span class="brand-name">Corvane<br>Cleaning Ltd</span>
  </div>
  <div class="contacts">
    <div class="row"><span class="item"><span class="ico"><svg viewBox="0 0 10 10"><rect x="1" y="2.5" width="8" height="5" fill="#fff"/></svg></span>hello@corvanecleaning.example</span></div>
    <div class="row">
      <span class="item"><span class="ico"><svg viewBox="0 0 10 10"><path d="M2 1h2l1 2-1 1a5 5 0 0 0 2 2l1-1 2 1v2c-4 0-7-3-7-7z" fill="#fff"/></svg></span>020 8837 2591</span>
      <span class="item"><span class="ico"><svg viewBox="0 0 10 10"><rect x="2" y="1" width="6" height="8" rx="1" fill="#fff"/></svg></span>020 8837 2604</span>
    </div>
    <div class="row"><span class="item"><span class="ico"><svg viewBox="0 0 10 10"><circle cx="5" cy="5" r="3.5" fill="none" stroke="#fff" stroke-width="1.3"/></svg></span>www.corvanecleaning.example</span></div>
    <div class="row"><span class="item"><span class="ico"><svg viewBox="0 0 10 10"><path d="M5 1a3 3 0 0 1 3 3c0 2-3 5-3 5S2 6 2 4a3 3 0 0 1 3-3z" fill="#fff"/></svg></span>Please provide full address of your company</span></div>
  </div>
</section>

<!-- Business card, back -->
<section class="sheet card-back" aria-label="Business card back">
  <svg class="waves" viewBox="0 0 290 188" preserveAspectRatio="none" aria-hidden="true">
    <path d="M0,150 C90,138 190,150 290,132 L290,188 L0,188 Z" fill="var(--blue-deep)"/>
    <path d="M0,146 C90,134 190,146 290,128 L290,132 C190,150 90,138 0,150 Z" fill="var(--blue-pale)"/>
  </svg>
  <div class="brand">
    <span class="brand-dot"></span>
    <span class="brand-name">Corvane<br>Cleaning Ltd</span>
  </div>
  <p class="tagline">cleaning • housekeeping • support services</p>
</section>

<!-- Business card, front -->
<section class="sheet card-front" aria-label="Business card front">
  <svg class="waves" viewBox="0 0 290 188" preserveAspectRatio="none" aria-hidden="true">
    <defs>
      <linearGradient id="cfWave" x1="0" y1="0" x2="1" y2="0">
        <stop offset="0" stop-color="var(--blue-light)"/>
        <stop offset="1" stop-color="var(--blue-deep)"/>
      </linearGradient>
    </defs>
    <path d="M0,50 C60,62 100,96 170,104 C220,109 260,114 290,122 L290,130 C250,122 210,120 160,118 C90,114 40,90 0,86 Z" fill="url(#cfWave)"/>
    <path d="M0,90 C40,94 90,118 160,122 C210,124 250,126 290,134 L290,137 C250,130 210,128 160,126 C90,124 40,100 0,94 Z" fill="var(--blue-pale)"/>
  </svg>
  <div class="brand">
    <span class="brand-dot"></span>
    <span class="brand-name">Corvane<br>Cleaning Ltd</span>
  </div>
  <div class="person">
    <p class="person-name">Owner Name</p>
    <p class="person-title">President</p>
  </div>
  <div class="contacts">
    <div class="row"><span class="item"><span class="ico"><svg viewBox="0 0 10 10"><path d="M2 1h2l1 2-1 1a5 5 0 0 0 2 2l1-1 2 1v2c-4 0-7-3-7-7z" fill="#fff"/></svg></span>020 8837 2591</span></div>
    <div class="row"><span class="item"><span class="ico"><svg viewBox="0 0 10 10"><rect x="2" y="1" width="6" height="8" rx="1" fill="#fff"/></svg></span>020 8837 2604</span></div>
    <div class="row"><span class="item"><span class="ico"><svg viewBox="0 0 10 10"><circle cx="5" cy="5" r="3.5" fill="none" stroke="#fff" stroke-width="1.3"/></svg></span>www.corvanecleaning.example</span></div>
    <div class="row"><span class="item"><span class="ico"><svg viewBox="0 0 10 10"><path d="M5 1a3 3 0 0 1 3 3c0 2-3 5-3 5S2 6 2 4a3 3 0 0 1 3-3z" fill="#fff"/></svg></span>Please provide full address of your company</span></div>
  </div>
</section>

<!-- Compliment slip -->
<section class="sheet slip" aria-label="Compliment slip">
  <span class="mark-faint"></span>
  <svg class="waves" viewBox="0 0 600 283" preserveAspectRatio="none" aria-hidden="true">
    <defs>
      <linearGradient id="slWave" x1="0" y1="0" x2="1" y2="1">
        <stop offset="0" stop-color="var(--blue-light)"/>
        <stop offset=".6" stop-color="var(--blue)"/>
        <stop offset="1" stop-color="var(--blue-deep)"/>
      </linearGradient>
    </defs>
    <path d="M50,0 L160,0 C200,80 280,150 420,205 C490,232 550,238 600,236 L600,283 L452,283 C428,255 400,205 356,160 C310,115 180,98 0,108 L0,100 C20,70 36,36 50,0 Z" fill="url(#slWave)"/>
    <path d="M0,115 C180,102 310,117 360,167 C400,207 430,260 456,290" fill="none" stroke="var(--blue-light)" stroke-width="5"/>
    <path d="M0,125 C180,112 305,127 352,175 C390,214 416,262 438,290" fill="none" stroke="var(--blue-pale)" stroke-width="4"/>
  </svg>
  <div class="brand">
    <span class="brand-dot"></span>
    <span class="brand-name">Corvane<br>Cleaning Ltd</span>
  </div>
  <div class="contacts">
    <div class="row">
      <span class="item"><span class="ico"><svg viewBox="0 0 10 10"><path d="M2 1h2l1 2-1 1a5 5 0 0 0 2 2l1-1 2 1v2c-4 0-7-3-7-7z" fill="#fff"/></svg></span>020 8837 2591</span>
    </div>
    <div class="row">
      <span class="item"><span class="ico"><svg viewBox="0 0 10 10"><rect x="1" y="2.5" width="8" height="5" fill="#fff"/></svg></span>hello@corvanecleaning.example</span>
      <span class="item"><span class="ico"><svg viewBox="0 0 10 10"><rect x="2" y="1" width="6" height="8" rx="1" fill="#fff"/></svg></span>020 8837 2604</span>
    </div>
    <div class="row">
      <span class="item"><span class="ico"><svg viewBox="0 0 10 10"><path d="M5 1a3 3 0 0 1 3 3c0 2-3 5-3 5S2 6 2 4a3 3 0 0 1 3-3z" fill="#fff"/></svg></span>Please provide full address of your company</span>
    </div>
    <div class="row">
      <span class="item"><span class="ico"><svg viewBox="0 0 10 10"><circle cx="5" cy="5" r="3.5" fill="none" stroke="#fff" stroke-width="1.3"/></svg></span>www.corvanecleaning.example</span>
    </div>
  </div>
</section>

</body>
</html>
```